Riddle of the Ivory Owl

We are hosting an open-to-the-public murder mystery dinner and masquerade ball on Oct. 31. I need a postcard design that we can display, hand out and mail for marketing.

We produce events in the KC area.

I'd like to see designs with a Halloween masquerade ball/murder mystery theme.

Events

```html
<!DOCTYPE html>
<html lang="en">
<head>
<meta charset="utf-8">
<title>Riddle of the Ivory Owl – Postcard Back</title>
<link rel="stylesheet" href="https://fonts.googleapis.com/css2?family=Source+Sans+3:wght@400;600;700&display=swap">
<style>
  :root {
    --backdrop: #cccccc;
    --card: #ffffff;
    --ink: #0d1820;
    --night: #0e1a21;
    --lime: #8cc63f;
    --rule: #c8c8c8;
    --muted: #6b6b6b;
    --blood: #d71f2a;
    --blood-deep: #b8141e;
  }
  html, body {
    margin: 0;
    width: 1200px;
    height: 900px;
    overflow: hidden;
    background: var(--backdrop);
    font-family: "Source Sans 3", "Source Sans Pro", sans-serif;
  }
  .postcard {
    position: absolute;
    left: 247px;
    top: 178px;
    width: 703px;
    height: 545px;
    background: var(--card);
    overflow: hidden;
  }
  .corner-band { position: absolute; left: 0; top: 0; }
  .brand {
    position: absolute;
    left: 18px;
    top: 30px;
    margin: 0;
    color: #ffffff;
    font-weight: 600;
    font-size: 22px;
    line-height: 1;
    white-space: nowrap;
  }
  .return-address {
    position: absolute;
    left: 235px;
    top: 70px;
    margin: 0;
    font-size: 10px;
    font-weight: 600;
    line-height: 13px;
    color: var(--ink);
    font-style: normal;
  }
  .stamp-box {
    position: absolute;
    left: 535px;
    top: 24px;
    width: 139px;
    height: 139px;
    border: 2px solid var(--rule);
    display: flex;
    align-items: center;
    justify-content: center;
    font-size: 10px;
    color: var(--muted);
  }
  .blood-splatter {
    position: absolute;
    left: 0;
    top: 268px;
    width: 92px;
    height: 170px;
    border-radius: 0 55% 48% 0 / 0 40% 60% 0;
    background: linear-gradient(160deg, var(--blood) 0%, var(--blood-deep) 100%);
  }
  .event-line {
    position: absolute;
    left: 93px;
    top: 251px;
    width: 180px;
    margin: 0;
    text-align: center;
    font-size: 19px;
    font-weight: 700;
    line-height: 23.3px;
    color: var(--ink);
  }
  .address-lines {
    position: absolute;
    left: 358px;
    top: 244px;
    width: 319px;
  }
  .address-lines span {
    display: block;
    height: 2px;
    background: var(--rule);
    margin-bottom: 46.5px;
  }
</style>
</head>
<body>
  <article class="postcard">
    <svg class="corner-band" width="230" height="180" viewBox="0 0 230 180" aria-hidden="true">
      <polygon points="0,0 218,0 0,175" fill="var(--lime)"/>
      <polygon points="0,0 195,0 0,160" fill="var(--night)"/>
    </svg>
    <p class="brand">Halden KC</p>

    <address class="return-address">Build, Street<br>Zip City<br>Country</address>

    <div class="stamp-box">stamp here</div>

    <div class="blood-splatter" role="img" aria-label="Splatter of red blood drops"></div>
    <p class="event-line">open-to-the-public murder mystery dinner and masquerade ball on Oct. 31.</p>

    <div class="address-lines"><span></span><span></span><span></span><span></span></div>
  </article>
</body>
</html>
```